Kit com 6 Layouts de Post para Redes Sociais (Facebook, Instagram e etc) + Capa de Facebookpara RZ SEGUROS E CONSORCIOS
Postado por: gestao.rzseguros_2840395726   Estou Offline

```html
<!DOCTYPE html>
<html lang="pt-BR">
<head>
<meta charset="UTF-8">
<title>RZ Seguros – Post</title>
<link href="https://fonts.googleapis.com/css2?family=Poppins:wght@400;500;600;700&display=swap" rel="stylesheet">
<style>
  :root{
    --purple-deep:#4a1f6e;
    --purple-mid:#6c2f8e;
    --purple-bright:#a852b6;
    --blush:#f6ecf6;
    --photo-dark:#3c4a33;
    --photo-light:#8a7f73;
    --white:#ffffff;
    --ink:#2d1a45;
  }
  *{margin:0;padding:0;box-sizing:border-box}
  html,body{width:1200px;height:1200px;overflow:hidden}
  body{font-family:'Poppins',sans-serif}
  .post{
    position:relative;width:1200px;height:1200px;overflow:hidden;
    background:linear-gradient(172deg,var(--purple-deep) 0%,var(--purple-mid) 35%,var(--purple-bright) 66%,var(--blush) 100%);
  }
  .decor{position:absolute;inset:0;width:1200px;height:1200px}
  .brand{
    position:absolute;left:912px;top:118px;
    color:var(--white);font-weight:500;font-size:38px;letter-spacing:0.5px;
  }
  .headline{
    position:absolute;right:58px;top:278px;
    color:var(--white);font-weight:600;font-size:82px;line-height:84px;
    text-align:right;letter-spacing:-1px;
  }
  .contact{
    position:absolute;right:58px;top:1036px;width:240px;
    color:var(--ink);text-align:center;
  }
  .contact .cta{font-size:18px;font-weight:500;letter-spacing:0.5px}
  .contact .phone{
    display:flex;align-items:center;justify-content:flex-end;gap:10px;
    font-size:28px;font-weight:700;margin-top:4px;
  }
  .contact .phone .xx{font-size:20px;font-weight:600}
  .contact .handle{
    display:flex;align-items:center;justify-content:flex-end;gap:8px;
    font-size:20px;font-weight:500;margin-top:6px;
  }
  .dot{width:18px;height:18px;border-radius:50%;background:var(--ink)}
</style>
</head>
<body>
<div class="post">
  <svg class="decor" viewBox="0 0 1200 1200" xmlns="http://www.w3.org/2000/svg">
    <defs>
      <linearGradient id="photoFill" x1="0" y1="0" x2="1" y2="1">
        <stop offset="0" stop-color="var(--photo-dark)"/>
        <stop offset="1" stop-color="var(--photo-light)"/>
      </linearGradient>
    </defs>
    <path role="img" aria-label="Foto de uma família sorrindo ao ar livre: pai carregando o filho nos ombros e mãe beijando a criança"
      d="M0 72 H670 Q712 72 700 110 L156 1200 H0 Z" fill="url(#photoFill)"/>
    <path d="M0 505 H120 Q150 505 138 535 L0 830" fill="none" stroke="var(--white)" stroke-width="3"/>
    <path d="M1160 696 H660 Q636 696 624 718 L336 1200" fill="none" stroke="var(--white)" stroke-width="3"/>
  </svg>

  <div class="brand">SUA LOGO</div>

  <h1 class="headline">Seu<br>Texto Aqui<br>Seu texto<br>aqui.</h1>

  <div class="contact">
    <div class="cta">LIGUE AGORA</div>
    <div class="phone">
      <svg width="30" height="30" viewBox="0 0 30 30" aria-hidden="true">
        <circle cx="15" cy="15" r="15" fill="var(--ink)"/>
        <path d="M10 9 q-2 2 0 6 q3 5 7 6 q3 1 4-1 l-2-3 -2 1 q-3-2-4-4 l1-2 z" fill="var(--white)"/>
      </svg>
      <span><span class="xx">xx.</span> 0000.0000</span>
    </div>
    <div class="handle"><span class="dot"></span>@RZSEGUROS</div>
  </div>
</div>
</body>
</html>
```